Zielgruppe
brinko handel ist eine Vertriebsagentur, die sich ausschließlich auf den BtoB Vertrieb spezialisiert hat. Wir agieren seit 19 Jahren am Markt und sind mehrfach ausgezeichneter Exzellenzberater des Mittelstandes. Wir unterstützen mittelständische Unternehmen, Familienunternehmen, Start up´s in der Wachstumsphase und Großkonzerne in der Industrie und im Dienstleistungsbereich. Ansprechpartner für uns sind Vertriebsleiter und GF´s in den Unternehmen.
Aufgabenstellung
Wir möchten unsere Angebotsvorlage neu im Layout neu designen lassen. Sie soll unsere Arbeitsweise zielgenau - authentisch - pfiffig widerspiegeln. Ich möchte gerne eine moderne und klare Struktur. Auf einer Seite sollen unsere USP´s dargestellt werden und auf ein - zwei Seiten ist das Angebot - in den folgenden Seiten sind die Vertragsinhalte.

```html
<!DOCTYPE html>
<html lang="de">
<head>
<meta charset="utf-8">
<title>brinko handel – Angebotsvorlage</title>
<link href="https://fonts.googleapis.com/css2?family=Exo+2:wght@400;600;700;800&family=Open+Sans:wght@400;600;700&family=Cormorant+Garamond:wght@300&display=swap" rel="stylesheet">
<style>
  :root{
    --blue:#1d8bd3;
    --grey:#c9c9c9;
    --dark:#3c3c3c;
    --text:#444;
    --white:#fff;
  }
  *{margin:0;padding:0;box-sizing:border-box}
  html,body{width:1200px;height:4258px;overflow:hidden;background:var(--white)}
  body{position:relative;font-family:"Open Sans",Arial,sans-serif;color:var(--text)}
  .abs{position:absolute}
  .head{font-family:"Exo 2",Arial,sans-serif;font-weight:800;color:var(--blue)}
  .panel{position:absolute;background:var(--grey)}
  .photo{position:absolute}
  .band{position:absolute;height:95px;background:var(--dark)}
  .band-title{position:absolute;width:600px;text-align:center;font-family:"Exo 2",Arial,sans-serif;font-weight:800;font-size:33px;color:var(--blue);letter-spacing:.5px}
  .brand{font-family:"Exo 2",Arial,sans-serif;font-weight:600;color:var(--blue);text-align:center}

  .cover-title{left:600px;top:72px;width:600px;text-align:center;font-size:44px}
  .cover-photo{left:752px;top:174px;width:296px;height:296px;border-radius:50%;background:radial-gradient(circle at 45% 40%,#e9e4e2 0%,#b9b3b4 45%,#6d3a3d 80%,#a92c33 100%)}

  .intro{left:0;top:848px;width:232px;height:615px;padding:50px 22px 0 28px}
  .intro-lead{font-family:"Exo 2",Arial,sans-serif;font-weight:800;color:var(--blue);font-size:16px;line-height:1.2;margin-bottom:22px}
  .intro p{color:var(--white);font-size:12.5px;line-height:1.55;text-align:justify;margin-bottom:20px}
  .benefit{position:absolute;width:104px;text-align:center}
  .benefit .dot{width:34px;height:34px;border-radius:50%;background:#a9a9a9;margin:0 auto 14px}
  .benefit h4{font-family:"Exo 2",Arial,sans-serif;font-weight:700;font-size:11px;color:var(--blue);line-height:1.15;margin-bottom:5px}
  .benefit p{font-size:8px;line-height:1.45;color:#555}

  .setup h3{font-family:"Exo 2",Arial,sans-serif;font-weight:800;font-size:22px;color:var(--blue);margin-bottom:8px}
  .setup p{font-size:11px;line-height:1.55;color:#555}
  .project{left:645px;top:1088px;width:512px;height:264px;border:2px solid var(--blue);padding:12px 16px}
  .project h3{font-family:"Exo 2",Arial,sans-serif;font-weight:800;font-size:22px;color:var(--blue);margin-bottom:8px}
  .project p,.project li{font-size:8px;line-height:1.5;color:#555}
  .project ul{list-style:none;margin:10px 0 10px 30px}
  .offer{left:630px;width:540px;text-align:center;font-size:10.5px;line-height:1.5;color:#333}
  .offer .hl{color:var(--blue);font-weight:600}

  .form-line{position:absolute;left:90px;font-size:14px;color:#444;font-family:"Exo 2",Arial,sans-serif}
  .rule{position:absolute;border-bottom:1px solid #666;height:0}
  .party h3{font-family:"Exo 2",Arial,sans-serif;font-weight:800;font-size:23px;color:var(--blue)}
  .party p{font-size:12px;line-height:2;color:var(--white)}

  .col{position:absolute;width:172px;font-size:9.4px;line-height:1.6;color:#444}
  .col h4{font-family:"Exo 2",Arial,sans-serif;font-weight:600;font-size:10px;color:var(--blue);margin:0 0 2px;line-height:1.3}
  .col h4 b{font-size:17px;font-weight:800;margin-right:3px}
  .col section{margin-bottom:12px}

  .final{left:637px;top:2705px;width:380px;font-size:9.6px;line-height:1.55;color:#444}
  .final h4{font-size:10px;font-weight:700;margin-bottom:12px}
  .final p{margin-bottom:12px}

  .service-dot{position:absolute;width:50px;height:50px;border-radius:50%;background:#a9a9a9;top:3826px}
  .service-list{position:absolute;left:40px;top:3905px;width:540px;font-size:10px;color:#333}
  .service-list p{height:23px;line-height:23px}
  .service-list .hl{color:var(--blue)}
  .service-list .in{padding-left:12px}
  .portrait{left:404px;top:4091px;width:150px;height:150px;border-radius:50%;background:#a9a9a9;z-index:2;display:flex;align-items:center;justify-content:center;font-size:11px;color:#333}
</style>
</head>
<body>

<!-- Cover -->
<div class="panel" style="left:600px;top:0;width:600px;height:700px"></div>
<h1 class="abs head cover-title">Hier steht z.B.ein Titel</h1>
<div class="photo cover-photo" role="img" aria-label="Foto: drei Geschäftsleute betrachten gemeinsam eine Broschüre"></div>
<div class="abs brand" style="left:600px;top:730px;width:600px;font-size:50px">brinko handel</div>

<!-- Vorteile / Projektarbeit -->
<div class="panel intro">
  <div class="intro-lead">brinko handel – seit 19 Jahren am Markt – hat sich auf die Kaltakquise und den Vertrieb im BtoB-Bereich spezialisiert –</div>
  <p>Wir sind der Turbo für Ihren Vertrieb und gehören zu den 10 führenden Anbietern im B2B-Vertrieb. Wir bewegen uns sicher in der Akquise in der oberen Führungsebene bis zum DAX-Konzern. Wir bieten eine 720° strukturierte Vertriebsberatung, -umsetzung und -kontrolle: von A (Analyse) – Z (Verkauf). Wir denken vor und zurück, reflektieren Gespräche und Zielgruppe.</p>
  <p>Wir sind zum 3. Mal in Folge als Exzellenzberater Deutscher Mittelstand im Vertrieb ausgezeichnet!</p>
</div>
<div class="photo" style="left:232px;top:848px;width:368px;height:215px;background:linear-gradient(160deg,#e3e3e3 0%,#f7f7f7 45%,#ffffff 70%,#eeeeee 100%)" role="img" aria-label="Foto: Schreibtisch mit Laptop, Kaffeetasse und Notizblock"></div>
<div class="abs head" style="left:250px;top:1030px;font-size:20px;font-weight:600">IHRE VORTEILE</div>
<div class="rule" style="left:400px;top:1050px;width:190px;border-color:#bbb"></div>

<div class="benefit" style="left:247px;top:1082px"><div class="dot"></div><h4>ENTSCHEIDER</h4><p>Wir führen 12.000 Gespräche im Monat mit Vorständen, Geschäftsführern, Marketing-, Vertriebs- und Einkaufsleitern</p></div>
<div class="benefit" style="left:357px;top:1082px"><div class="dot"></div><h4>RICHTIGER ZEITPUNKT</h4><p>Wir haben das Fingerspitzengefühl beim Interessenten zum richtigen Zeitpunkt der Entscheidung präsent zu sein, ohne penetrant zu wirken</p></div>
<div class="benefit" style="left:467px;top:1082px"><div class="dot"></div><h4>VERTRIEBSAFFIN</h4><p>Kompetenz und vor allem Erfahrungen im Vertrieb lassen uns schnell und zielsicher für Sie agieren. Wir wissen wie wir die richtigen Ansprechpartner kontaktieren und auch begeistern können.</p></div>
<div class="benefit" style="left:247px;top:1250px"><div class="dot"></div><h4>ENTSCHEIDER</h4><p>Wir führen 12.000 Gespräche im Monat mit Vorständen, Geschäftsführern, Marketing-, Vertriebs- und Einkaufsleitern</p></div>
<div class="benefit" style="left:357px;top:1268px"><div class="dot"></div><h4>ENTSCHEIDER</h4><p>Wir führen 12.000 Gespräche im Monat mit Vorständen, Geschäftsführern, Marketing-, Vertriebs- und Einkaufsleitern</p></div>
<div class="benefit" style="left:467px;top:1278px"><div class="dot"></div><h4>ENTSCHEIDER</h4><p>Wir führen 12.000 Gespräche im Monat mit Vorständen, Geschäftsführern, Marketing-, Vertriebs- und Einkaufsleitern</p></div>
<div class="benefit" style="left:247px;top:1415px"><div class="dot"></div><h4>ENTSCHEIDER</h4><p>Wir führen 12.000 Gespräche im Monat mit Vorständen, Geschäftsführern, Marketing-, Vertriebs- und Einkaufsleitern</p></div>
<div class="benefit" style="left:357px;top:1435px"><div class="dot"></div><h4>ENTSCHEIDER</h4><p>Wir führen 12.000 Gespräche im Monat mit Vorständen, Geschäftsführern, Marketing-, Vertriebs- und Einkaufsleitern</p></div>

<div class="abs setup" style="left:628px;top:872px;width:560px">
  <h3>SETUP-Installation einmalig</h3>
  <p>2 h Workshop – Einweisung Mitarbeiterin 2h (1)<br>Abstimmung Prozesse und Schnittstellen<br>Erarbeitung + Coaching Gesprächskonzept / Einwandargumentation</p>
</div>
<div class="abs setup" style="left:628px;top:988px;width:560px">
  <h3>TECHNIK-Programmierung einmalig</h3>
  <p>Integration firmeninterner Telefonnummer</p>
</div>
<div class="abs project">
  <h3>PROJEKTARBEIT</h3>
  <p>agieren unter Kessler Global Logistics SE &amp; Co. KG<br>akquirieren auf Entscheiderebene in den Unternehmen Einkauf, Qualitätsmanager, Produktionsleiter stellen das Unternehmen mit seinen Dienstleistungen und Vorteilen vor und erfragen</p>
  <ul>
    <li>- aktuellen Bedarf an Logistik</li>
    <li>- wiederkehrende und herausfordernde Destinationen inkl. Tonnagen</li>
    <li>- Zufriedenheit mit dem aktuellen Partner erfassen, die aktuelle IST-Situation und erfragen ggf. bestehende Partnerschaften / Verträge wecken Interesse an den Dienstleistungen und bauen ein vertrauensvolles Verhältnis auf</li>
    <li>- erarbeiten bedarfsorientierte Wiedervorlagen,</li>
    <li>- koordinieren und bestätigen Termine vor Ort,</li>
    <li>- bleiben am vertriebsorientiert dran Kontakt,</li>
    <li>- erfragen Alternativangebote</li>
  </ul>
  <p>telefonieren aktiv Angeboten nach und erfragen die Entscheidergründe</p>
</div>
<div class="abs offer" style="top:1390px">
  <div class="hl">Adressrecherche / Adressdaten inkl. Kontaktdaten</div>
  <div style="font-weight:600">Adresselektion nach Unternehmen, Branchen und Regionen</div>
</div>
<div class="abs offer" style="top:1452px">
  <div class="hl">a) TESTPROJEKT – 15h / Woche – 10 Wochen</div>
  <div>14h Akquise/ Recherche + 2h interne Projektabstimmung je Woche</div>
  <div>garantiert 140 Gespräche / Woche</div>
</div>
<div class="abs offer" style="top:1530px">
  <div class="hl">b) TESTPROJEKT - 20h / Woche – 10 Wochen</div>
  <div>18,5h Akquise/ Recherche + 1,5h interne Projektabstimmung je Woche garantiert 185 Gespräche / Woche</div>
</div>

<div class="band" style="left:0;top:1603px;width:1200px"></div>
<div class="band-title" style="left:0;top:1636px">NEUE MÄRKTE EROBERN</div>
<div class="band-title" style="left:600px;top:1630px">NEUE KUNDEN AKQUIRIEREN</div>

<!-- Angebotsbestätigung / Vertrag -->
<div class="photo" style="left:0;top:1698px;width:600px;height:105px;background:linear-gradient(170deg,#c4c4c4 0%,#e6e6e6 35%,#f7f7f7 60%,#eef2f0 100%)" role="img" aria-label="Foto: Tastatur und Kaffeetasse auf hellem Schreibtisch"></div>
<div class="photo" style="left:0;top:1900px;width:62px;height:390px;background:linear-gradient(90deg,#dfe3e2,#f4f6f5)" role="img" aria-label="Foto: aufgeschlagenes Notizbuch mit Spiralbindung"></div>

<div class="form-line" style="top:1808px;line-height:1.35"><b>Auftraggeber</b><br>Kessler Global Logistics SE &amp; Co. KG</div>
<div class="form-line" style="top:1912px;line-height:1.35"><b>Auftragnehmer</b><br>brinko handel GmbH<br>Ahornstraße 5<br>91052 Erlangen</div>
<div class="form-line" style="top:2015px;width:470px;line-height:1.4">Hiermit bestätige ich als Auftraggeber das Angebot-Nr. 20221108 und erteile entsprechend dem Angebot den Auftrag an brinko handel GmbH.</div>
<div class="form-line" style="left:162px;top:2100px;line-height:1.4">Variante a - 15h Vertriebsunterstützung / Woche<br>Variante b - 20h Vertriebsunterstützung / Woche</div>
<div class="form-line" style="top:2188px">Ort, Datum:</div>
<div class="rule" style="left:172px;top:2206px;width:398px"></div>
<div class="form-line" style="top:2270px">Name/Vorname in Druckbuchstaben:</div>
<div class="rule" style="left:335px;top:2288px;width:235px"></div>
<div class="form-line" style="top:2323px">Unterschrift:</div>
<div class="rule" style="left:172px;top:2341px;width:398px"></div>
<div class="form-line" style="top:2407px">Firmenstempel</div>
<div class="rule" style="left:185px;top:2425px;width:385px"></div>

<div class="panel" style="left:600px;top:1698px;width:600px;height:218px"></div>
<div class="abs party" style="left:637px;top:1730px">
  <h3>Auftraggeber</h3>
  <p>Kessler Global Logistics SE &amp; Co. KG</p>
</div>
<div class="abs party" style="left:998px;top:1766px">
  <h3>Auftragnehmer</h3>
  <p>brinko handel GmbH<br>Marlene Vogt-Brandt<br>Ahornstraße 5<br>91052 Erlangen</p>
</div>

<div class="col" style="left:637px;top:1940px">
  <section><h4><b>§ 1</b>Vertragsgegenstand</h4><p>Der AN unterstützt den AG bei der Akquise neuer Kunden.</p></section>
  <section><h4><b>§ 2</b>Leistungen/ Vergütung des AN</h4><p>Siehe Seite LEISTUNGEN</p></section>
  <section><h4><b>§ 3</b>Pflichten des AG</h4><p>(1) Der AG verpflichtet sich, dem AN rechtzeitig, vollständig und korrekt die zur Ausübung seiner Tätigkeit erforderlichen Unterlagen, Druckerzeugnisse u. o. vorkonfektionierte Briefumschläge zum Versand an die Interessenten inkl. Porto, unentgeltlich zur Verfügung zu stellen.</p><p>(2) Der AG schuldet sämtliche für die Durchführung der o.g. Leistungen des AN notwendigen Informationen.</p><p>(3) Der AG hat dem AN Zugang zu seiner Kundenkartei zu Akquisezwecken zu gewähren. Der AG sichert zu, dass er die Gewähr dafür übernimmt, dass</p></section>
</div>
<div class="col" style="left:827px;top:1940px">
  <section><p>bei dem gesamten von ihm zur Verfügung gestellten Adressen eine telefonische Kontaktaufnahme mit dem Kunden/Nichtkunden gestattet ist.</p></section>
  <section><h4><b>§ 4</b>Zahlungsvereinbarung</h4><p>(1) Der AN erhält für seine Tätigkeit eine Pauschalvergütung wie in § 2 definiert zzgl. gesetzl. MwSt.</p><p>(2) Der in Rechnung gestellte Betrag ist innerhalb von 14 Tagen an die bekanntgegebenen Bankverbindungen ohne Abzüge zu überweisen.</p><p>(3) Verrechnungsschecks werden nicht akzeptiert.</p><p>(4) Jährliche Kostenanpassung anhand des Arbeitskostenindex - Der vereinbarte Pauschalpreis je Monat wird im Folgejahr im Januar entsprechend der Entwicklung des Arbeitskostenindex angepasst. Die Entwicklung des Arbeitskostenindex laut Statistischem Bundesamt wird entsprechend der prozentualen Veränderung berechnet.</p></section>
</div>
<div class="col" style="left:1018px;top:1940px">
  <section><h4><b>§ 5</b>Vertragsdauer, Vertragsende</h4><p>(1) Dieser Vertrag hat eine feste Laufzeit von 10 Wochen ab Beginn Workshop. Er verlängert er sich stillschweigend jeweils um 3 Monate, wenn er nicht von einem der Vertragspartner mit einer Frist von 1 Woche zum Vertragsende schriftlich gekündigt wird.</p><p>(2) Der AG erhält ein Sonderkündigungsrecht nach 3 Wochen der Zusammenarbeit innerhalb 1 Woche.</p><p>(3) Das Recht zur Kündigung aus wichtigem Grund bleibt unberührt. Der AN ist zur Kündigung aus wichtigem Grund berechtigt, wenn der AG mit der Zahlung der Vergütung gemäß § 5 dieses Vertrags mit mehr als zwei Wochen in Rückstand gerät.</p></section>
</div>

<div class="band" style="left:0;top:2463px;width:1200px;height:92px"></div>
<div class="band-title" style="left:0;top:2492px">ANGEBOTSBESTÄTIGUNG</div>
<div class="band-title" style="left:600px;top:2492px">VERTRAGSBESTANDTEILE</div>

<!-- weitere Vertragsbestandteile -->
<div class="panel" style="left:0;top:2555px;width:600px;height:264px"></div>
<div class="abs" style="left:90px;top:2640px;font-family:'Cormorant Garamond',serif;font-weight:300;font-size:30px;color:var(--white);letter-spacing:1px">TEXT ODER BILD MÖGLICH</div>

<div class="col" style="left:35px;top:2835px">
  <section><h4><b>§ 6</b>Haftung</h4><p>(1) Der AN haftet unbeschränkt bei Vorsatz oder grober Fahrlässigkeit, für die Verletzung von Leben, Leib oder Gesundheit, nach den Vorschriften des Produkthaftungsgesetzes sowie im Umfang einer vom AN übernommenen Garantie.</p><p>(2) Bei leicht fahrlässiger Verletzung einer Pflicht, die wesentlich für die Erreichung des Vertragszwecks ist (Kardinalpflicht), ist die Haftung des AN der Höhe nach begrenzt auf den Schaden, der nach der Art des fraglichen Geschäfts vorhersehbar und typisch ist.</p><p>(3) Eine weitergehende Haftung des AN besteht, soweit gesetzlich zulässig, nicht.</p><p>(4) Die vorstehende Haftungsbeschränkung gilt auch für die persönliche Haftung der Mitarbeiter, Vertreter und Organe des AN.</p></section>
</div>
<div class="col" style="left:227px;top:2835px">
  <section><h4><b>§ 7</b>Geheimhaltung</h4><p>(Beide Vertragsparteien verpflichten sich gegenseitig zur vertraulichen Behandlung aller ihr bei der Zusammenarbeit bekanntwerdenden Geschäftsinterna, soweit diese nicht offenkundig sind oder aufgrund gesetzlicher Verpflichtungen oder auf Anordnung eines Gerichtes oder einer Behörde offen gelegt werden müssen. Die Pflicht zur vertraulichen Behandlung besteht auch über die Dauer des Vertragsverhältnisses hinaus.</p></section>
  <section><h4><b>§ 8</b>Abwerbungs- und Beschäftigungsverbot</h4><p>(1) Die Vertragsparteien verpflichten sich, während der Dauer des Projektes bzw. der Dauer der festgelegten Zusammenarbeit sowie innerhalb eines Jahres nach dessen Beendigung keine Mitarbeiter</p></section>
</div>
<div class="col" style="left:418px;top:2835px">
  <section><p>des anderen Vertragspartners abzuwerben oder zu beschäftigen, und zwar gleichgültig ob als Angestellte, freie Mitarbeiter oder eines beauftragten dritten Unternehmens. Das Abwerbe- und Beschäftigungsverbot gilt für alle abhängigen oder verbundenen Unternehmen des AG und analog des AN.</p><p>(2) Verstößt eine Vertragspartei gegen vorstehende Regelung, so hat sie für jeden Fall der Zuwiderhandlung eine Vertragsstrafe in Höhe von € 15.000,00 an die andere Vertragspartei zu zahlen. Schadenersatzansprüche bleiben hiervon unberührt.</p></section>
  <section><h4><b>§ 9</b>Referenznennung</h4><p>Der AN ist berechtigt, den AG als Referenzkunden zu benennen.</p></section>
</div>

<div class="photo" style="left:995px;top:2555px;width:205px;height:150px;background:linear-gradient(200deg,#f2f4ea 0%,#e6ecd2 40%,#ffffff 100%)" role="img" aria-label="Foto: weiße Gänseblümchen und gelbe Blüten"></div>
<div class="photo" style="left:1020px;top:2840px;width:180px;height:200px;background:radial-gradient(circle at 60% 55%,#a9d4cd 0%,#cfe6e2 55%,#ffffff 100%)" role="img" aria-label="Foto: mintfarbene Teekanne"></div>
<div class="photo" style="left:1045px;top:3080px;width:100px;height:200px;background:linear-gradient(90deg,#f1f3f2 0%,#f1f3f2 85%,#7cc3b7 85%,#7cc3b7 100%)" role="img" aria-label="Foto: kariertes Notizbuch mit mintfarbenem Gummiband"></div>

<div class="abs final">
  <h4>§ 10 Sonstige Bestimmungen</h4>
  <p>(1) Mündliche Nebenabreden zu diesem Vertrag bestehen nicht.</p>
  <p>(2) Änderungen und/oder Ergänzungen zu diesem Vertrag bedürfen zu ihrer Wirksamkeit der Schriftform. Mündliche Vereinbarungen über die Aufhebung der Schriftform sind nichtig.</p>
  <p>(3) Sollten einzelne Bestimmungen dieses Vertrages ganz oder teilweise unwirksam oder undurchführbar sein oder werden, so wird hierdurch die Gültigkeit der übrigen Bestimmungen nicht berührt. Anstelle der unwirksamen oder undurchführbaren Bestimmung ist eine neue wirksame und durchführbare Bestimmung in gehöriger Form zu vereinbaren, die dem Zweck der unwirksamen Bestimmung möglichst nahekommt. Das gleiche gilt im Falle einer Regelungslücke mit der Maßgabe, dass eine neue wirksame und durchführbare Bestimmung in gehöriger Form zu vereinbaren ist, die dem entspricht, was die Vertragsparteien zum Zeitpunkt des Vertragsschlusses geregelt haben würden, wenn sie die Lückenhaftigkeit erkannt hätten.</p>
  <p>(4) Erfüllungsort und Gerichtsstand ist Erlangen</p>
</div>
<div class="abs" style="left:637px;top:3137px;font-size:10.5px;font-weight:700;color:#444">Vertragsbestandteile gelesen, akzeptiert und Auftrag erteilt.</div>
<div class="abs" style="left:637px;top:3188px;font-size:10.5px;font-weight:600;color:#444">Ort, Datum:</div>
<div class="rule" style="left:705px;top:3201px;width:290px"></div>
<div class="abs" style="left:637px;top:3238px;font-size:10.5px;font-weight:600;color:#444">Unterschrift Auftraggeber:</div>
<div class="rule" style="left:775px;top:3251px;width:220px"></div>

<div class="band" style="left:0;top:3315px;width:600px;height:90px"></div>
<div class="band-title" style="left:0;top:3342px;width:auto;padding-left:102px;text-align:left">VERTRAGSBESTANDTEILE</div>

<!-- Abschlussseite -->
<div class="photo" style="left:0;top:3405px;width:600px;height:356px;background:linear-gradient(100deg,#b8b2aa 0%,#d9d4cd 30%,#efece8 55%,#c9c2b8 80%,#8f877d 100%)" role="img" aria-label="Foto: Geschäftsführerin in weißer Bluse steht lächelnd in einem Besprechungsraum"></div>
<div class="abs" style="left:40px;top:3792px;font-family:'Exo 2',Arial,sans-serif;font-weight:700;font-size:13.5px;color:var(--blue)">Ihre Vertriebsagentur mit Know How und Unterstützung in</div>
<div class="service-dot" style="left:41px"></div>
<div class="service-dot" style="left:124px"></div>
<div class="service-dot" style="left:220px"></div>
<div class="service-dot" style="left:319px"></div>
<div class="service-dot" style="left:413px"></div>

<div class="service-list">
  <p class="hl" style="font-family:'Exo 2',Arial,sans-serif;font-weight:800;font-size:13px">BtoB</p>
  <p>- aktive Kundenbetreuung und –informationen</p>
  <p>- Kundenbefragungen mit Mehrwert</p>
  <p>- dynamische und automatisierte Leadgenerierung und Betreuung</p>
  <p class="hl">- BtoB Kundenimpuls®</p>
  <p class="in">Weg von der Kaltakquise –Wer sucht online gezielt nach Ihrer Dienstleistung?</p>
  <p class="in" style="width:360px;white-space:nowrap;overflow:visible">Wir wissen wo, wie und wann – wir bleiben automatisiert und persönlich an Ihren Kunden dran!</p>
  <p class="hl">- brinko-Checker®</p>
  <p class="in">Der neue Weg zur Leadgenerierung im BtoB Vertrieb.</p>
  <p class="in">Den ersten Testmonat gratis.</p>
</div>

<div class="abs portrait">Portrait</div>

<div class="band" style="left:0;top:4165px;width:600px;height:93px"></div>
<div class="abs brand" style="left:80px;top:4178px;width:310px;font-size:28px">brinko handel</div>
<div class="abs" style="left:140px;top:4228px;font-size:9px;font-weight:600;color:var(--white)">Name Straße PLZ Ort Telefonnummer website</div>

</body>
</html>
```